Custom fitness equipment builder needs a Flyer

We need a single-sided 8.5x11 (inch) flyer to promote our business. The business name is 'Granite Forge' - we build custom equipment for weightlifting, CoreDrill, and other fitness and sport training facilities. In general the equipment is all steel with fully-welded construction and is designed or at least tailored specifically for the client.

The flyer should convey the heavy-duty nature of the equipment (durability) as well the individualized, custom nature of the build process. This does not necessarily need to be entirely through words. In fact, a relatively minimal amount of text is preferred, as often times potential customers may first see the company and the flyer in the middle of a competition, in which they are likely to be preoccupied, exhausted, sweaty, and/or hungry!

Example text could be:

"Never Settle. You don't strive for good enough in your training or your coaching. Why settle for it in your equipment? Granite Forge designs and hand builds custom equipment for your needs and your space."

It should invite people to visit our website at www.granite-forge.example and to email us at mike@granite-forge.example

Inclusion of Facebook (GraniteForge) and Instagram (graniteforge) links is preferred, but not required. A clean, uncluttered, attention-grabbing design is the priority.

Photos of previously built equipment as well as a welding picture from our shop are included. .svg files of our logo options are also included. Both the "stylized barbell" as well as the Granite Forge script should be included on the flyer, but they do not necessarily need to be together. The flyer may be either full color or B/W. The Granite Forge script and logo should be either all black or all white.

Note that my printer uses a 8.625x11.125 design w/ 0.0625 bleeds all around to cut down to the 8.5x11 final size.

Target Market(s)

Owners, managers, and coaches of weightlifting, CoreDrill, fitness, and sport training facilities. Athletes with home gyms. Not in general "globo gyms" such as Kell's Club, Orbit Wellness, etc.

Industry/Entity Type

Fitness Equipment

Requirements
Must have
• Direct people to get more info by going to website www.granite-forge.example and send email to mike@granite-forge.example
Nice to have
• Facebook (GraniteForge) and Instagram (graniteforge) links.
Should not have
• Too much text / clutter.

```html
<!DOCTYPE html>
<html lang="en">
<head>
<meta charset="utf-8">
<title>Granite Forge – Never Settle Flyer</title>
<link href="https://fonts.googleapis.com/css2?family=Oswald:wght@400;500;700&family=Roboto:wght@400;500&display=swap" rel="stylesheet">
<style>
  :root {
    --page-bg: #ececec;
    --poster-black: #121212;
    --poster-dark: #1c1c1c;
    --ring-dark: #2a2a2a;
    --orange: #f07a1e;
    --amber: #f5a81c;
    --yellow: #f2e51a;
    --white: #ffffff;
    --text-light: #f2f2f2;
    --bar-gray: #474747;
    --rule-gray: #8a8a8a;
  }
  * { margin: 0; padding: 0; box-sizing: border-box; }
  html, body {
    width: 1124px; height: 1200px; overflow: hidden;
    background: var(--page-bg);
  }
  .flyer {
    position: absolute; left: 111px; top: 20px;
    width: 901px; height: 1160px; overflow: hidden;
    background: radial-gradient(ellipse at 60% 40%, var(--poster-dark), var(--poster-black) 70%);
    font-family: "Roboto", sans-serif;
    box-shadow: 0 6px 18px rgba(0,0,0,.25);
  }
  .flyer-art { position: absolute; inset: 0; }
  .brand-name {
    position: absolute; left: 600px; top: 62px; width: 290px;
    text-align: center; color: var(--white);
    font-family: "Oswald", sans-serif; font-weight: 500;
    font-size: 40px; line-height: 46px; letter-spacing: 3px;
    text-transform: uppercase;
  }
  .pitch {
    position: absolute; left: 38px; top: 806px; width: 825px;
    color: var(--text-light); font-size: 24.5px; line-height: 32.5px;
    text-align: justify; text-align-last: justify;
  }
  .contact {
    position: absolute; left: 0; top: 1030px; width: 901px;
    color: var(--text-light); font-size: 19px; line-height: 25.5px;
    text-align: center;
  }
  .contact-line { display: flex; justify-content: center; align-items: center; gap: 5px; }
  .contact-line svg { width: 15px; height: 15px; }
  .social {
    position: absolute; top: 1114px; left: 0; width: 901px;
    display: flex; justify-content: center; gap: 100px;
    color: var(--text-light); font-size: 20px;
  }
  .social-item { display: flex; align-items: center; gap: 8px; }
  .social-dot { width: 22px; height: 22px; border-radius: 50%; background: var(--white); }
</style>
</head>
<body>
<div class="flyer">
  <svg class="flyer-art" width="901" height="1160" viewBox="0 0 901 1160">
    <defs>
      <linearGradient id="badge-fill" x1="0" y1="0" x2="1" y2="0">
        <stop offset="0" stop-color="var(--orange)" stop-opacity="0"/>
        <stop offset="0.35" stop-color="var(--orange)"/>
        <stop offset="1" stop-color="var(--yellow)"/>
      </linearGradient>
      <linearGradient id="ring-fill" x1="0" y1="0" x2="0.3" y2="1">
        <stop offset="0" stop-color="var(--orange)"/>
        <stop offset="0.5" stop-color="var(--amber)"/>
        <stop offset="1" stop-color="var(--yellow)"/>
      </linearGradient>
      <linearGradient id="photo-fill" x1="0" y1="0" x2="1" y2="1">
        <stop offset="0" stop-color="#2e2f33"/>
        <stop offset="0.55" stop-color="#1d1e21"/>
        <stop offset="1" stop-color="#3a2423"/>
      </linearGradient>
      <linearGradient id="steel-fill" x1="0" y1="0" x2="0" y2="1">
        <stop offset="0" stop-color="#d9d9d9"/>
        <stop offset="0.5" stop-color="#9d9d9d"/>
        <stop offset="1" stop-color="#cfcfcf"/>
      </linearGradient>
      <linearGradient id="corner-fill" x1="0" y1="0" x2="0" y2="1">
        <stop offset="0" stop-color="#b59a12"/>
        <stop offset="1" stop-color="var(--yellow)"/>
      </linearGradient>
    </defs>

    <!-- welcome badge -->
    <g class="welcome-badge">
      <path d="M470 387 H868 a16 16 0 0 1 16 16 V503 a16 16 0 0 1 -16 16 H470 Z" fill="url(#badge-fill)"/>
    </g>

    <!-- hero circle -->
    <g class="hero-circle">
      <circle cx="298" cy="285" r="340" fill="var(--ring-dark)" opacity="0.85"/>
      <circle cx="298" cy="285" r="310" fill="url(#ring-fill)"/>
      <circle cx="298" cy="285" r="288" fill="var(--white)"/>
      <circle cx="298" cy="285" r="276" fill="url(#photo-fill)" role="img" aria-label="Athlete training on a leg press machine in a dim gym"/>
    </g>

    <g class="welcome-text" font-family="Oswald, sans-serif" text-anchor="end" fill="#111">
      <text x="857" y="432" font-size="40" font-weight="700">WELCOME TO</text>
      <text x="857" y="471" font-size="27" font-weight="400">GRANITE FORGE</text>
      <text x="857" y="506" font-size="25" font-weight="400">&amp; thanks for visiting!</text>
    </g>

    <!-- headline -->
    <text class="headline" x="38" y="786" font-family="Oswald, sans-serif" font-weight="700" font-size="172"
          textLength="825" lengthAdjust="spacingAndGlyphs" fill="url(#steel-fill)">NEVER SETTLE</text>

    <!-- call bar -->
    <g class="call-bar">
      <polygon points="131,993 170,924 905,924 862,993" fill="var(--bar-gray)"/>
      <polygon points="190,918 845,918 841,924 186,924" fill="var(--amber)"/>
      <polygon points="825,918 865,918 820,999 804,999" fill="var(--yellow)"/>
      <text x="174" y="982" font-family="Oswald, sans-serif" font-weight="700" font-size="47" fill="var(--white)">CALL US NOW! <tspan fill="var(--yellow)">(555) 018-2746</tspan></text>
    </g>

    <!-- footer -->
    <g class="footer">
      <rect x="0" y="1020" width="901" height="140" fill="#191919"/>
      <polygon points="0,969 0,1160 196,1160" fill="url(#corner-fill)"/>
      <polygon points="901,965 901,1160 701,1160" fill="url(#corner-fill)"/>
      <line x1="60" y1="1020" x2="842" y2="1020" stroke="var(--rule-gray)" stroke-width="2"/>
    </g>
  </svg>

  <div class="brand-name">Granite<br>Forge</div>

  <p class="pitch">You don't strive for good enough in your training or your coaching. Why settle for it in your equipment? Granite Forge designs and hand builds custom equipment for your needs and your space.</p>

  <div class="contact">
    <div class="contact-line">
      <svg viewBox="0 0 16 16"><path d="M8 1a5 5 0 0 0-5 5c0 4 5 9 5 9s5-5 5-9a5 5 0 0 0-5-5zm0 7a2 2 0 1 1 0-4 2 2 0 0 1 0 4z" fill="#fff"/></svg>
      4310-B Quarry Mill Road, Ashbrook, MD
    </div>
    <div class="contact-line">
      <svg viewBox="0 0 16 16"><rect x="1" y="3.5" width="14" height="9" fill="#fff"/><path d="M1 3.5 8 9l7-5.5" fill="none" stroke="#191919" stroke-width="1.3"/></svg>
      mike@granite-forge.example
    </div>
    <div class="contact-line">
      <svg viewBox="0 0 16 16" fill="none" stroke="#fff" stroke-width="1.2"><circle cx="8" cy="8" r="6.5"/><ellipse cx="8" cy="8" rx="3" ry="6.5"/><line x1="1.5" y1="8" x2="14.5" y2="8"/></svg>
      www.granite-forge.example
    </div>
  </div>

  <div class="social">
    <div class="social-item"><span class="social-dot"></span>graniteforge</div>
    <div class="social-item"><span class="social-dot"></span>GraniteForge</div>
  </div>
</div>
</body>
</html>
```